Pinwheel Ads Creative In 3 Different Sizes For Marketing Agency

We need a set of ads designed that will be used to run ads for lead generation on pinwheel and LM Newsfeed.
So we need the news feed for PW and LM image size and a Carousel Ad size for a total of 3 sizes of same design.
Please reference these links for specs for files:
https://www.pinwheelsocial.example/business/ads-guide/carousel
https://www.pinwheelsocial.example/business/ads-guide/image
https://www.pinwheelsocial.example/business/ads-guide/image/lumora-feed
Content on ad:
HEADLINE; 2x-5x YOUR SALES & LEADS OVERNIGHT
SUBHEADLINE: OFFER COMPLIMENTARY HOTEL STAYS & $100 DINING CARDS AS A BONUS FOR BUYING YOUR PRODUCT OR SERVICE
(without having to personally fulfill or pay for them yourself!)
Target Market(s)
business owners
Industry/Entity Type
digital marketing agency
Colors
Designer to choose colors to be used in the design.
Requirements
Must have
- Must use my website theme. Feel free to steal images from my website and use them. @ www.harborlanebrightgroup.biz I have included an example of what someone else designed for me as inspiration that I kind of like but im looking for something way better too so please do not copy this one.
Nice to have
- Want to keep theme of website so when they click it and go to my website they kknow they are in the right place so everything is consistent
Should not have
- should not use stock images only use images from my website @ www.harborlanebrightgroup.biz

```html
<!DOCTYPE html>
<html lang="en">
<head>
<meta charset="utf-8">
<title>2X-5X Your Sales &amp; Leads Overnight – Harbor Lane Bright Group</title>
<link rel="stylesheet" href="https://fonts.googleapis.com/css2?family=Arimo:wght@400;700&display=swap">
<style>
  :root {
    --violet-deep: #231b62;
    --violet-shield: #2e2a6e;
    --violet-photo-a: #2f2a70;
    --violet-photo-b: #4a44a0;
    --white: #ffffff;
    --growth-green: #1fe84c;
    --footer-light: #f2f2f2;
    --footer-grey: #d9d9d9;
    --brand-blue: #1f78c1;
    --ink: #111111;
  }
  html, body {
    margin: 0;
    padding: 0;
    width: 1200px;
    height: 1200px;
    overflow: hidden;
    background: var(--white);
  }
  .ad {
    position: relative;
    width: 1200px;
    height: 1200px;
    overflow: hidden;
    font-family: "Arimo", Arial, sans-serif;
  }
  .ad__art {
    position: absolute;
    inset: 0;
    display: block;
  }
  .headline text,
  .offer text,
  .brand text {
    font-family: "Arimo", Arial, sans-serif;
  }
  .headline text { fill: var(--white); font-weight: 700; }
  .offer text { fill: var(--white); font-weight: 400; }
  .offer .strong { font-weight: 700; }
  .brand__name { fill: var(--brand-blue); font-weight: 700; }
  .brand__url { fill: var(--ink); font-weight: 400; }
</style>
</head>
<body>
<main class="ad">
  <svg class="ad__art" width="1200" height="1200" viewBox="0 0 1200 1200" xmlns="http://www.w3.org/2000/svg">
    <defs>
      <linearGradient id="photoTone" x1="0" y1="0" x2="1" y2="1">
        <stop offset="0" stop-color="var(--violet-photo-a)"/>
        <stop offset="1" stop-color="var(--violet-photo-b)"/>
      </linearGradient>
      <linearGradient id="cardsTone" x1="0" y1="0" x2="1" y2="1">
        <stop offset="0" stop-color="#4a3e6a"/>
        <stop offset="1" stop-color="#c98a5a"/>
      </linearGradient>
      <linearGradient id="footerTone" x1="0" y1="0" x2="0" y2="1">
        <stop offset="0" stop-color="var(--footer-grey)"/>
        <stop offset="1" stop-color="var(--footer-light)"/>
      </linearGradient>
    </defs>

    <rect class="scene-photo" x="0" y="0" width="1200" height="830" fill="url(#photoTone)"
          role="img" aria-label="Photo of a business team working together around a table, tinted violet"/>

    <rect class="rewards-collage" x="60" y="380" width="520" height="420" rx="14" fill="url(#cardsTone)" opacity="0.85"
          role="img" aria-label="Fanned reward cards: dining card, getaway, cruise, hotel savings, fitness watch and roundtrip airfare gift box"/>

    <path class="growth-band" d="M0 821 L121 790 L264 802 L417 753 L569 743 L722 728 L868 774 L1023 728 L1166 705 L1200 700 L1200 994 L0 994 Z" fill="var(--violet-deep)"/>
    <polyline class="growth-line" points="0,821 121,790 264,802 417,753 569,743 722,728 868,774 1023,728 1166,705 1200,700"
              fill="none" stroke="var(--growth-green)" stroke-width="7" stroke-linejoin="round"/>
    <g class="growth-nodes" fill="var(--white)" stroke="var(--growth-green)" stroke-width="9">
      <circle cx="121" cy="790" r="23"/>
      <circle cx="264" cy="802" r="23"/>
      <circle cx="417" cy="753" r="23"/>
      <circle cx="569" cy="743" r="23"/>
      <circle cx="722" cy="728" r="23"/>
      <circle cx="868" cy="774" r="23"/>
      <circle cx="1023" cy="728" r="23"/>
      <circle cx="1166" cy="705" r="23"/>
    </g>

    <path class="shield shield--frame" d="M300 0 L901 0 L901 420 C901 560 770 680 600 680 C430 680 300 560 300 420 Z" fill="var(--white)"/>
    <path class="shield shield--fill" d="M330 0 L871 0 L871 420 C871 545 755 650 600 650 C445 650 330 545 330 420 Z" fill="var(--violet-shield)"/>

    <g class="headline" text-anchor="start">
      <text x="384" y="185" font-size="164" textLength="433" lengthAdjust="spacingAndGlyphs">2X-5X</text>
      <text x="389" y="279" font-size="74" textLength="443" lengthAdjust="spacingAndGlyphs">YOUR SALES</text>
      <text x="576" y="361" font-size="78" textLength="47" lengthAdjust="spacingAndGlyphs">&amp;</text>
      <text x="486" y="451" font-size="74" textLength="230" lengthAdjust="spacingAndGlyphs">LEADS</text>
      <text x="399" y="536" font-size="74" textLength="404" lengthAdjust="spacingAndGlyphs">OVERNIGHT</text>
    </g>

    <g class="offer">
      <text x="60" y="885" font-size="38" textLength="1080" lengthAdjust="spacingAndGlyphs">OFFER COMPLIMENTARY <tspan class="strong">HOTEL STAYS &amp; $100 DINING CARDS</tspan></text>
      <text x="114" y="928" font-size="38" textLength="971" lengthAdjust="spacingAndGlyphs">AS A BONUS FOR BUYING YOUR PRODUCT OR SERVICE</text>
      <text x="199" y="972" font-size="27" textLength="793" lengthAdjust="spacingAndGlyphs">(without having to personally fulfill or pay for them yourself!)</text>
    </g>

    <rect class="footer" x="0" y="994" width="1200" height="206" fill="url(#footerTone)"/>
    <g class="brand">
      <circle cx="250" cy="1080" r="20" fill="var(--brand-blue)"/>
      <text class="brand__name" x="288" y="1097" font-size="46" textLength="685" lengthAdjust="spacingAndGlyphs">HARBOR LANE BRIGHT GROUP</text>
      <text class="brand__url" x="600" y="1173" font-size="34" text-anchor="middle" textLength="576" lengthAdjust="spacingAndGlyphs">www.harborlanebrightgroup.biz</text>
    </g>
  </svg>
</main>
</body>
</html>
```